Scented Candle Company Sticker Design for Packaging

We need a Sticker design for our various scented candle packages. Our handmade candles incorperate hand crafted Chiyogami Paper imported from Japan, which is wrapped around the jar. Each of the scents have different papers assigned to them and although we would like a general design in which the text can be changed according to each scent we would also like if the beautiful Japanese paper designs could be subtly incorporated in the design.

We want the the text of the sticker and logo of our company to be printed in gold foil once printed and our featured logo image is of a Dogwood tree. We think that perhaps the inclusion of dogwood blossom/s might look nice in the design but is not a must have!

We are fond of the delicate and classic print designs and etching designs. We would also like the design to be in a portrait rectangle that is closer in the shape of a square/ or not too long of a rectangle, and, would like to have a boarder on the edge of the sticker (this could incorporate the blossom if you wish, I have attached an image for reference/ inspiration) but we are after something much more simplistic and draws less attention to the eye and connected in the boarder.

Our brand is elegant and classic and we would like to be in keeping with our style. We have attached some images of the candles and our logo for inspiration, we do not want the stickers for the candle themselves but rather to place on the packaging.

Ive left some information for one of the candle scents for this design but once again I would like to reiterate that the design should allow for interchangeable titles for the other fragrances.

Moonlit Petal Garden(in smaller writing).
Moonlit Petal Garden, Orange blossom, cinnamon.

Our candles are hand made in Australia and a made from 100% soy wax and we would like to to be presented on the label.

I would like to mention again that we are looking for an elegant and classic design. We are looking for a simplistic design/layout that also focuses on the fine details. It should be striking but also not overbearing with an air of sophistication with minimal to no use of colours in encouraged.

I have also attached a font that is matched to the "candle co." underneath the tree in the logo.
Updates

I only just posted the design request, but first created the brief on the 2nd. I would like more time for the designers to both see my review and have an adequate amount of time to work on the project.

Target Market(s)

Up Market Shoppers.

Font styles to use
Script
Other font styles liked:
• Acorn

Colors
fbfbfb

Requirements
Must have
• Logo on the sticker.
Nice to have
• Nice to have a dogwood blossom incorporated into the boarder but must be simplistic as it doesn't want to be the main focus of the sticker
Should not have
• Photographs in the sticker design. Must be graphic design. No to little colour.

```html
<!DOCTYPE html>
<html lang="en">
<head>
<meta charset="utf-8">
<title>Linden Candle Co. – Moonlit Petal Garden Label</title>
<link rel="stylesheet" href="https://fonts.googleapis.com/css2?family=Cormorant+Garamond:wght@500&family=Poiret+One&display=swap">
<style>
  :root {
    --canvas: #ffffff;
    --paper: #fbfbfb;
    --gold-light: #d9c67a;
    --gold: #b8a045;
    --gold-deep: #9c8433;
  }
  * { box-sizing: border-box; margin: 0; padding: 0; }
  html, body {
    width: 1200px;
    height: 1200px;
    overflow: hidden;
    background: var(--canvas);
  }
  .canvas {
    position: relative;
    width: 1200px;
    height: 1200px;
  }
  .label {
    position: absolute;
    left: 240px;
    top: 169px;
    width: 720px;
    height: 862px;
  }
  .label__border {
    position: absolute;
    inset: 0;
    width: 100%;
    height: 100%;
  }
  .label__panel {
    position: absolute;
    left: 42px;
    top: 30px;
    right: 42px;
    bottom: 30px;
    background: var(--paper);
    border-radius: 6px;
  }
  .brand {
    position: absolute;
    left: 0;
    right: 0;
    top: 152px;
    text-align: center;
    color: var(--gold);
    font-family: "Cormorant Garamond", serif;
    font-weight: 500;
  }
  .brand__mark {
    display: block;
    width: 80px;
    height: 80px;
    margin: 0 auto 26px;
    border-radius: 50%;
    background: var(--gold);
  }
  .brand__name {
    display: block;
    font-size: 46px;
    letter-spacing: 0.14em;
    line-height: 1;
  }
  .brand__sub {
    display: block;
    margin-top: 8px;
    font-size: 13px;
    letter-spacing: 0.2em;
    line-height: 1;
  }
  .scent {
    position: absolute;
    left: 0;
    right: 0;
    top: 510px;
    text-align: center;
    color: var(--gold);
    font-family: "Poiret One", sans-serif;
    font-size: 36px;
    line-height: 50px;
  }
</style>
</head>
<body>
  <main class="canvas">
    <section class="label">
      <svg class="label__border" viewBox="0 0 720 862" role="img" aria-label="Gold foil border with delicate blossom branches along the edges">
        <defs>
          <linearGradient id="gold-foil" x1="0" y1="0" x2="1" y2="1">
            <stop offset="0" stop-color="#d9c67a"/>
            <stop offset="0.5" stop-color="#b8a045"/>
            <stop offset="1" stop-color="#9c8433"/>
          </linearGradient>
        </defs>
        <rect x="0" y="0" width="720" height="862" fill="url(#gold-foil)"/>
      </svg>
      <div class="label__panel">
        <div class="brand">
          <span class="brand__mark" aria-hidden="true"></span>
          <span class="brand__name">LINDEN</span>
          <span class="brand__sub">CANDLE CO.</span>
        </div>
        <p class="scent">Moonlit<br>Petal Garden</p>
      </div>
    </section>
  </main>
</body>
</html>
```